vintage glimmory thank you postcard

I am wanting to use this postcard for my wedding thank you. My theme is: outdoor, rustic, country, vintage, neutral colored. The photo booth at my wedding was in a grain bin on a old victorian couch photos taken with a digital glimmory camera! I want the post card to look like an old fashioned glimmory picture with the border and all. At the bottom saying "thank you" or "Rex and Nadia," "Harwell Wedding", "June 14, 2014," something to that affect. On the back left side leaving room for me to write a personal message thanking them for the help/gift/support. The back right side left for the name and address. I will add a wedding picture of the two of us to the front (from our wedding day). Anything that gives the post card a vintage old time feeling is great!! I have a general idea of what I want but, now I know you guys can take care of the rest for me! :) thank you in advance!! -Nadia

Target Market(s)

family, friends - all ages!

Industry/Entity Type

Wedding

Requirements
Must have
• "glimmory photo" look
vintage
"Thank you"
"Rex and Nadia"
Nice to have
• June 14, 2014

```html
<!DOCTYPE html>
<html lang="en">
<head>
<meta charset="utf-8">
<title>Harwell Wedding – Thank You Postcard</title>
<link href="https://fonts.googleapis.com/css2?family=Parisienne&family=Special+Elite&family=Handlee&family=Nothing+You+Could+Do&display=swap" rel="stylesheet">
<style>
  :root {
    --backdrop: #554b43;
    --wood-light: #a9c2a6;
    --wood-mid: #8fa98b;
    --band: #b9c9ab;
    --band-soft: rgba(196, 210, 182, 0.88);
    --ink-brown: #74472b;
    --frame-cream: #efe6d2;
    --frame-edge: #d9ccb0;
    --photo-warm: #8c7f62;
    --photo-sepia: #6f6255;
    --card-white: #ffffff;
    --address-ink: #5a5a5a;
    --flower-sage: #c4cdb3;
    --divider: #2a2a2a;
  }
  * { margin: 0; padding: 0; box-sizing: border-box; }
  html, body { width: 927px; height: 1200px; overflow: hidden; }
  body { background: var(--backdrop); position: relative; }

  /* Front of postcard */
  .card-front {
    position: absolute; left: 15px; top: 15px; width: 582px; height: 750px;
    overflow: hidden;
  }
  .wood-texture {
    position: absolute; inset: 0;
    background: linear-gradient(90deg, var(--wood-mid) 0%, var(--wood-light) 30%, var(--wood-mid) 55%, var(--wood-light) 80%, var(--wood-mid) 100%);
  }
  .title-band {
    position: absolute; left: 0; top: 22px; width: 100%; height: 185px;
    background: var(--band);
  }
  .title {
    position: absolute; left: 0; top: 42px; width: 100%; text-align: center;
    font-family: "Parisienne", cursive; font-size: 112px; font-weight: 400; line-height: 1;
    color: var(--ink-brown); letter-spacing: 1px; white-space: nowrap;
  }

  .print {
    position: absolute; background: var(--frame-cream);
    border: 1px solid var(--frame-edge);
    box-shadow: 2px 3px 6px rgba(0,0,0,0.35);
  }
  .print-main { left: 73px; top: 185px; width: 464px; height: 350px; }
  .print-main .photo {
    position: absolute; left: 20px; top: 24px; width: 425px; height: 254px;
    background: radial-gradient(ellipse at 60% 45%, #b7a27a 0%, var(--photo-warm) 55%, #4e4a3c 100%);
  }
  .print-caption {
    position: absolute; left: 26px; top: 302px;
    font-family: "Handlee", cursive; font-size: 21px; line-height: 26px;
    color: var(--ink-brown); white-space: nowrap;
  }
  .print-small { width: 120px; height: 146px; }
  .print-small .photo {
    position: absolute; left: 9px; top: 10px; width: 100px; height: 104px;
    background: radial-gradient(ellipse at 50% 45%, #a59684 0%, var(--photo-sepia) 70%, #4a4038 100%);
  }
  .print-small.one { left: 310px; top: 470px; transform: rotate(-2deg); }
  .print-small.two { left: 423px; top: 498px; transform: rotate(2.5deg); }

  .wedding-line {
    position: absolute; left: 92px; top: 576px;
    font-family: "Special Elite", monospace; font-size: 15px; line-height: 19px;
    letter-spacing: 2.5px; color: var(--ink-brown); text-align: center;
  }

  .message-band {
    position: absolute; left: 0; top: 636px; width: 100%; height: 98px;
    background: var(--band-soft);
  }
  .message {
    position: absolute; left: 0; top: 644px; width: 100%; text-align: center;
    font-family: "Handlee", cursive; font-size: 12.5px; line-height: 22px;
    color: var(--ink-brown);
  }

  /* Back of postcard */
  .card-back {
    position: absolute; left: 340px; top: 750px; width: 561px; height: 434px;
    background: var(--card-white);
  }
  .return-address {
    position: absolute; left: 37px; top: 30px;
    font-family: "Nothing You Could Do", cursive; font-size: 10px; line-height: 20px;
    font-style: normal; color: var(--address-ink);
  }
  .flower-art {
    position: absolute; left: 0; top: 70px; width: 130px; height: 300px;
    background: radial-gradient(ellipse at 40% 45%, var(--flower-sage) 0%, rgba(196,205,179,0.35) 55%, rgba(255,255,255,0) 80%);
    opacity: 0.7;
  }
  .back-divider {
    position: absolute; left: 270px; top: 137px; width: 1.5px; height: 217px;
    background: var(--divider);
  }
</style>
</head>
<body>
  <section class="card-front">
    <div class="wood-texture" role="img" aria-label="Weathered mint green painted barn wood with peeling paint"></div>
    <div class="title-band"></div>
    <h1 class="title">Thank You</h1>

    <figure class="print print-main">
      <div class="photo" role="img" aria-label="Wedding photo of the couple at the window of a vintage truck with wildflowers"></div>
      <figcaption class="print-caption">Rex and Nadia Harwell</figcaption>
    </figure>

    <figure class="print print-small one">
      <div class="photo" role="img" aria-label="Sepia wedding photo of the couple outdoors"></div>
    </figure>
    <figure class="print print-small two">
      <div class="photo" role="img" aria-label="Sepia close-up wedding photo of the couple"></div>
    </figure>

    <p class="wedding-line">HARWELL WEDDING<br>JUNE 14, 2014</p>

    <div class="message-band"></div>
    <p class="message">
      A loving note can barely express how you added to our happiness on this magical day.<br>
      We would like to send our sincerest thanks for your thoughts, your gifts and your presence in our lives!<br>
      ♡ love Rex &amp; Nadia ♡
    </p>
  </section>

  <section class="card-back">
    <address class="return-address">
      Mr. and Mrs. Harwell<br>
      118 N Maple Street<br>
      Elmdale, KS 66850
    </address>
    <div class="flower-art" role="img" aria-label="Faint sage line drawing of wildflowers"></div>
    <div class="back-divider"></div>
  </section>
</body>
</html>
```